Business Card Design Project

Hi. We need a new business card for Brightfield Partners, a consultancy that helps people with online marketing strategy and solutions.

We have a new logo and now need the info presented - front and back of business card.

FRONT

Logo

Online strategy, consulting and coaching
Varlo Admarket consulting
Search Engine Optimisation
Internet Lead Generation
Domain name broking

BACK

Tom Bradwell-Jones
+ 61 83215 9076
+ 61 (0) 418 536 207
tom@brightfieldpartners.com.au
www.brightfieldpartners.com.au

Talkora: tombradwelljones
PO Box 312, South Perth, Western Australia 6951

Target Market(s)

Business owners, corporates

Industry/Entity Type

Marketing

Requirements
Must have
• double sided
size: 86 x 54mm
supplied as one pdf with crop marks shown (+- 1mm, with 2-3 mm bleed)

```html
<!DOCTYPE html>
<html lang="en">
<head>
<meta charset="utf-8">
<title>Brightfield Partners – Business Card</title>
<link rel="stylesheet" href="https://fonts.googleapis.com/css2?family=Arimo:wght@400;700&display=swap">
<style>
  :root {
    --page: #ffffff;
    --frame: #6f6f6f;
    --edge-blue: #6fb3d8;
    --mint: #dfeed9;
    --mint-pale: #f4f9f2;
    --panel: rgba(255,255,255,0.82);
    --ink: #1f1f1f;
    --brand-blue: #2c4f8f;
    --box-top: #9ea897;
    --box-bottom: #d6e5cc;
    --box-line: #7c8479;
    --name: #ffffff;
  }
  * { box-sizing: border-box; margin: 0; padding: 0; }
  html, body { width: 936px; height: 1200px; overflow: hidden; background: var(--page); }
  body { position: relative; font-family: "Arimo", Arial, sans-serif; color: var(--ink); }

  .card { position: absolute; border: 1px solid var(--frame); background: var(--page); }
  .card-front { left: 0; top: 0; width: 923px; height: 580px; overflow: hidden; }
  .card-back  { left: 13px; top: 620px; width: 923px; height: 580px; overflow: hidden; }

  .front-field { position: absolute; left: 0; top: 0; }

  .logo-panel {
    position: absolute; left: 55px; top: 57px; width: 281px; height: 177px;
    border-radius: 40px; background: var(--panel);
    display: flex; align-items: center; justify-content: center; gap: 10px;
  }
  .logo-mark { width: 22px; height: 22px; border-radius: 50%; background: var(--brand-blue); }
  .logo-name { font-size: 24px; font-weight: 700; color: var(--brand-blue); }

  .services-panel {
    position: absolute; left: 447px; top: 318px; width: 453px; height: 223px;
    border-radius: 44px; background: var(--panel);
  }
  .services { list-style: none; position: absolute; left: 487px; top: 346px; }
  .services li { font-size: 22.6px; line-height: 32px; white-space: nowrap; }

  .side-strip { position: absolute; top: 0; width: 40px; height: 580px;
    background: linear-gradient(to bottom, var(--mint-pale), var(--mint)); }
  .side-strip.left { left: 0; }
  .side-strip.right { right: 0; width: 42px; }

  .contact-box {
    position: absolute; left: 180px; top: 175px; width: 565px; height: 241px;
    border: 1px solid var(--box-line); border-radius: 24px 24px 0 0;
    background: linear-gradient(to bottom, var(--box-top), var(--box-bottom) 70%);
    box-shadow: 6px 10px 18px rgba(0,0,0,0.28);
    text-align: center; padding-top: 42px;
  }
  .contact-name { font-size: 29px; font-weight: 700; color: var(--name); line-height: 36px; margin-bottom: 2px; }
  .contact-line { font-size: 22px; line-height: 25px; white-space: nowrap; }
  .contact-line.tight { letter-spacing: -0.3px; }
</style>
</head>
<body>
  <section class="card card-front" aria-label="Card front">
    <svg class="front-field" width="923" height="580" viewBox="0 0 923 580" aria-hidden="true">
      <defs>
        <linearGradient id="fieldFade" x1="0" y1="0" x2="1" y2="0">
          <stop offset="0" stop-color="#dcecd6"/>
          <stop offset="0.6" stop-color="#e9f3e5"/>
          <stop offset="1" stop-color="#ffffff"/>
        </linearGradient>
      </defs>
      <path d="M22 558 V110 Q22 20 112 20 H810 Q900 20 900 110 V558 Z"
            fill="url(#fieldFade)" stroke="var(--edge-blue)" stroke-width="1.5"/>
    </svg>

    <div class="logo-panel">
      <span class="logo-mark"></span>
      <span class="logo-name">Brightfield Partners</span>
    </div>

    <div class="services-panel"></div>
    <ul class="services">
      <li>Online strategy, consulting and coaching</li>
      <li>Varlo Admarket consulting</li>
      <li>Search Engine Optimisation</li>
      <li>Internet Lead Generation</li>
      <li>Domain name broking</li>
    </ul>
  </section>

  <section class="card card-back" aria-label="Card back">
    <div class="side-strip left"></div>
    <div class="side-strip right"></div>
    <div class="contact-box">
      <p class="contact-name">Tom Bradwell-Jones</p>
      <p class="contact-line">+61 83215 9076</p>
      <p class="contact-line">+61 (0) 418 536 207</p>
      <p class="contact-line">tom@brightfieldpartners.com.au</p>
      <p class="contact-line tight">www.brightfieldpartners.com &nbsp;talkora : tombradwelljones</p>
      <p class="contact-line">PO. Box 312, Harlow Bay, Western Australia 6958</p>
    </div>
  </section>
</body>
</html>
```